Harwick Structure Works needs a Business card design and logo

We Need a business card design and logo for a Building & Construction business based in Melbourne. We work in both the Domestic & Commercial sector. We specialize in all aspects of building including extensions, Renovations, and alterations. Construction Management, Project Management, And labour hire

Industry/Entity Type

Business

```html
<!DOCTYPE html>
<html lang="en">
<head>
<meta charset="utf-8">
<title>Harwick Structure Works – Business Card</title>
<link rel="stylesheet" href="https://fonts.googleapis.com/css2?family=Exo+2:wght@400;500;600;700;800&display=swap">
<style>
  :root {
    --page-bg: #ffffff;
    --card-bg: #ffffff;
    --card-border: #7d7d7f;
    --band-grey: #a6a7ab;
    --band-red: #cf222a;
    --ink: #231f20;
    --accent-red: #cf222a;
    --mark-dark: #231f20;
  }
  * { box-sizing: border-box; margin: 0; padding: 0; }
  html, body {
    width: 1200px; height: 1000px; overflow: hidden;
    background: var(--page-bg);
    font-family: "Exo 2", sans-serif;
    color: var(--ink);
  }
  .canvas { position: relative; width: 1200px; height: 1000px; }
  .business-card {
    position: absolute; left: 360px; top: 320px;
    width: 519px; height: 320px;
    background: var(--card-bg);
    border: 1px solid var(--card-border);
    overflow: hidden;
  }
  .service-band {
    position: absolute; left: 0; width: 100%; height: 54px;
    display: flex; align-items: center; justify-content: center;
    color: #fff; font-weight: 500; letter-spacing: 2.6px;
  }
  .service-band--top { top: 0; background: var(--band-grey); font-size: 22px; }
  .service-band--bottom { bottom: 0; background: var(--band-red); font-size: 22px; }
  .brand-mark {
    position: absolute; left: 33px; top: 64px;
    width: 60px; height: 64px; background: var(--mark-dark);
  }
  .brand-name {
    position: absolute; left: 112px; top: 70px;
    font-size: 29px; font-weight: 800; letter-spacing: -0.4px;
    line-height: 1; color: var(--ink); white-space: nowrap;
  }
  .brand-tagline {
    position: absolute; left: 113px; top: 108px;
    font-size: 16px; font-weight: 400; letter-spacing: 3.1px;
    line-height: 1; color: var(--accent-red); white-space: nowrap;
  }
  .contact {
    position: absolute; left: 112px; top: 148px;
    font-size: 15px; line-height: 25.5px; white-space: nowrap;
  }
  .contact-name { font-size: 19px; font-weight: 600; margin-bottom: 4px; line-height: 26px; }
  .contact-role { font-size: 15px; font-weight: 400; }
</style>
</head>
<body>
<main class="canvas">
  <section class="business-card">
    <div class="service-band service-band--top">EXTENTIONS • RENOVATIONS</div>

    <div class="brand-mark" aria-hidden="true"></div>
    <div class="brand-name">Harwick Structure Works</div>
    <div class="brand-tagline">Domestic &amp; Commercial Builders</div>

    <div class="contact">
      <p class="contact-name">Daniel Harwick, <span class="contact-role">Principal</span></p>
      <p class="contact-line">Mobile: 0412 555 318</p>
      <p class="contact-line">Office: (03) 9555 01842</p>
      <p class="contact-line">Email: info@harwickstructureworks.com</p>
    </div>

    <div class="service-band service-band--bottom">ALTERATIONS • DECKS • PERGOLAS</div>
  </section>
</main>
</body>
</html>
```